Business Card and Letterhead for Vantel Psychology

We need a business card design and letterhead to use for our Psychology firm that specializes in psychoeducational assessments and individual therapy. Our motto is Purpose-Driven Assessments, Meaning-Centered Therapy.Our contact information is as follows:
Vantel Psychology
The Bramwick Block - 4127-38St.
Box 6154 Carrowdale, WM
T2K 3R8
t 555.555.0148 (VANT)
f 555.555.0193
www.vantelpsych-example.ca
The business card will be used for two different psychologists so I can supply names nearer to completion. We prefer clean, uncluttered looks.

Target Market(s)

Clients, Educators

Font styles to use
Sans Serif

Colors

Designer to choose colors to be used in the design.

Requirements
Must have
• All relevant contact info, logo, some "white" space.
Nice to have
• It would be nice to see letterhead options that have the logo on the top of the page but also options that have it on the side. I think top of the page is probably our preference.
Should not have
• Too much clutter!

```html
<!DOCTYPE html>
<html lang="en">
<head>
<meta charset="utf-8">
<title>Vantel Psychology Letterhead</title>
<link rel="stylesheet" href="https://fonts.googleapis.com/css2?family=Roboto:wght@400;500&display=swap">
<style>
  :root {
    --backdrop: #e4e5e7;
    --paper: #f4f4f4;
    --ink: #1d1d1d;
    --brand-blue: #5bbfdd;
    --brand-orange: #f5a04a;
    --watermark: #e7e7e7;
    --signature-tone: #d2d2d2;
  }
  * { box-sizing: border-box; margin: 0; padding: 0; }
  html, body {
    width: 1200px; height: 1200px; overflow: hidden;
    background: var(--backdrop);
    font-family: "Roboto", Arial, sans-serif;
    color: var(--ink);
  }
  .letterhead {
    position: absolute; left: 200px; top: 34px;
    width: 800px; height: 1132px;
    background: var(--paper);
    overflow: hidden;
    box-shadow: 0 6px 24px rgba(0,0,0,0.12);
  }
  .brand {
    position: absolute; left: 90px; top: 96px;
    display: flex; align-items: center; gap: 12px;
  }
  .brand-dot {
    width: 34px; height: 34px; border-radius: 50%;
    background: var(--brand-blue);
  }
  .brand-name {
    font-size: 22px; font-weight: 400; letter-spacing: 2px;
    text-transform: uppercase; color: var(--brand-blue);
  }
  .watermark {
    position: absolute; right: -150px; top: 600px;
    width: 420px; height: 420px; border-radius: 50%;
    border: 46px solid var(--watermark);
  }
  .letter {
    position: absolute; left: 90px; top: 300px; width: 600px;
    font-size: 13.5px; line-height: 1.45;
  }
  .letter p { margin-bottom: 16px; }
  .letter .date { margin-bottom: 14px; }
  .letter .recipient { margin-bottom: 18px; }
  .letter .closing { margin-bottom: 4px; }
  .signature {
    width: 150px; height: 58px; margin: 6px 0 4px;
    background: linear-gradient(90deg, var(--signature-tone), #e2e2e2);
    border-radius: 4px;
  }
  .footer-rule {
    position: absolute; left: 0; right: 0; bottom: 50px; height: 3px;
    background: var(--brand-orange);
  }
  .footer {
    position: absolute; left: 0; right: 0; bottom: 0; height: 42px;
    background: var(--brand-blue);
    display: flex; flex-direction: column; justify-content: center; align-items: flex-end;
    gap: 2px; padding-right: 40px;
    font-size: 11.5px; font-weight: 500; color: #111; line-height: 1.2;
  }
  .footer .contacts { display: flex; gap: 16px; align-items: center; }
  .footer .contacts span { display: inline-flex; align-items: center; gap: 4px; }
  .footer svg { width: 10px; height: 10px; }
</style>
</head>
<body>
  <main class="letterhead">
    <div class="brand">
      <div class="brand-dot"></div>
      <div class="brand-name">Vantel Psychology</div>
    </div>

    <div class="watermark"></div>

    <section class="letter">
      <p class="date">August 1, 2018</p>
      <p class="recipient">Marcus Ellery<br>Manager<br>Tarnwell Company<br>71 Birch Lane, Ste 9<br>Harlow Springs, Wisconsin 54199</p>
      <p>Dear Marcus,</p>
      <p>I'm writing to resign my position as customer service representative, effective August 15, 2018.</p>
      <p>I've recently decided to go back to school, and my program starts in early September. I'm tendering my resignation now so that I can be as helpful as possible to you during the transition.</p>
      <p>I've truly enjoyed my time working with you and everyone else on our team at Tarnwell. It's rare to find a customer service role that offers as much opportunity to grow and learn and such a positive, inspiring team of people to grow and learn with.</p>
      <p>I'm particularly grateful for your guidance while I was considering furthering my education. Your support has meant so much to me.</p>
      <p>Please let me know if there's anything I can do to help you find and train my replacement.</p>
      <p class="closing">Thanks, and best wishes,</p>
      <div class="signature" role="img" aria-label="Handwritten signature of Renata Fields"></div>
      <p>Renata Fields</p>
    </section>

    <div class="footer-rule"></div>
    <footer class="footer">
      <div class="address">The Bramwick Block - 4127-38St. Box 6154 Carrowdale, WM T2K 3R8</div>
      <div class="contacts">
        <span><svg viewBox="0 0 10 10"><path d="M2 1l2 2-1 1.2a6 6 0 0 0 2.8 2.8L7 6l2 2-1.2 1.4C4.5 9.4.6 5.5.6 2.2z" fill="#111"/></svg>555.555.0148 (VANT)</span>
        <span><svg viewBox="0 0 10 10"><rect x="1" y="3" width="8" height="5" rx="1" fill="#111"/><rect x="3" y="1" width="4" height="2.5" fill="#111"/></svg>555.555.0193</span>
        <span><svg viewBox="0 0 10 10"><circle cx="5" cy="5" r="4" fill="none" stroke="#111"/><path d="M1 5h8M5 1c-2 2.5-2 5.5 0 8M5 1c2 2.5 2 5.5 0 8" fill="none" stroke="#111" stroke-width=".8"/></svg>www.vantelpsych-example.ca</span>
      </div>
    </footer>
  </main>
</body>
</html>
```